Software company WebSite Design (enterprise level SW, Mobile apps, HW prototypes)

We need design for our new webpages. We got new logo and new business cards and we need webdesign which will be match with those two.
We are dealing with corporate level software development - enterprise level portals, development of optimalization SW, route planning optimalizations. For a few months we are developing mobile applications for companies.
IMPORTANT is to express the cutting edge technological company.

Target Market(s)

IT company customers

Industry/Entity Type

Business

Number of Pages Required

2 page

Requirements
Must have
• Project needs to have landing page and product detail page. Design needs to be created including full font and example images as there would be a real webpage. Design should be clean, modern and expressing hi-tech level of the company.
• Example of well designer web pages - www.quorvelt.com, www.brandissa.com - We like the font formatting and font designs (colors, placing, etc - its professional).
• Attached image contains screenshot from old web landing page. It contains basic sections of our business (Simulation Tools, Enterprise Intranet Systems, Hi-tech web presentations, Supporting Enterprise services - Optimalization and logistics monitoring)

```html
<!DOCTYPE html>
<html lang="en">
<head>
<meta charset="utf-8">
<title>Enterprise Software</title>
<link rel="stylesheet" href="https://fonts.googleapis.com/css2?family=Roboto+Slab:wght@300;400;700&display=block">
<style>
:root{
  --teal:#2cb6c0;
  --teal-dark:#1b7585;
  --navy:#163c7c;
  --blue-band:#0b3f88;
  --blue-deep:#061f4a;
  --pale:#e3f5f6;
  --grey:#9a9a9a;
  --white:#ffffff;
}
*{margin:0;padding:0;box-sizing:border-box}
html,body{width:1200px;height:1200px;overflow:hidden;background:var(--white)}
body{font-family:"Roboto Slab","Rockwell","Zilla Slab",serif;position:relative}
.abs{position:absolute}
.top-strip{left:0;top:0;width:1200px;height:22px;background:#eef9fa}
.products{left:0;top:22px;width:1200px;height:408px;background:linear-gradient(90deg,#27aab5,#2fbac3 50%,#29b0ba)}
.section-title{left:238px;top:50px;font-size:24px;font-weight:700;color:var(--teal-dark);white-space:nowrap;letter-spacing:-.2px}
.nav-arrows{display:flex;gap:4px}
.nav-arrows svg{width:19px;height:19px}
.card{width:181px;background:var(--white);text-align:center}
.card .media{margin:4px;height:172px}
.product-card{top:101px;height:294px}
.product-name{margin-top:13px;font-size:14.5px;font-weight:700;color:var(--navy);white-space:nowrap;letter-spacing:-.2px}
.starting{margin-top:2px;font-size:9.5px;font-weight:300;color:var(--grey)}
.price{margin-top:1px;font-size:25px;font-weight:300;color:var(--teal);line-height:30px}
.shop{display:inline-block;margin-top:5px;width:82px;height:23px;line-height:21px;border:1px solid var(--navy);font-size:10px;color:var(--navy)}
.testimonial{left:0;top:430px;width:1200px;height:330px;background:
  radial-gradient(ellipse 380px 180px at 75% 60%,rgba(40,110,200,.55),transparent 70%),
  radial-gradient(ellipse 340px 160px at 22% 45%,rgba(25,85,170,.5),transparent 70%),
  linear-gradient(100deg,var(--blue-deep),var(--blue-band) 30%,#0e4d9e 60%,var(--blue-deep))}
.avatar{left:538px;top:464px;width:124px;height:124px;border-radius:50%;border:3px solid var(--teal);background:radial-gradient(circle at 50% 35%,#d9b49c 0 18%,transparent 19%),linear-gradient(180deg,#f2f4f6 0,#dfe5ea 55%,#253047 70%,#1a2333)}
.person{left:0;width:1200px;text-align:center;color:var(--white);white-space:nowrap}
.person-name{top:598px;font-size:18px;font-weight:300}
.person-role{top:620px;font-size:10px;font-weight:700}
.quote{left:305px;top:651px;width:590px;text-align:center;color:var(--white);font-size:13px;font-weight:300;line-height:15px}
.dots{left:564px;top:719px;display:flex;gap:6px}
.dots span{width:7px;height:7px;border-radius:50%;background:var(--white)}
.dots span.dim{background:#6f8fbf}
.portfolio{left:0;top:760px;width:1200px;height:440px;background:linear-gradient(160deg,#f2fbfb,var(--pale) 55%,#cfeff1)}
.portfolio-kicker{left:0;top:802px;width:1200px;text-align:center;font-size:24px;font-weight:700;color:var(--navy)}
.portfolio-title{left:0;top:822px;width:1200px;text-align:center;font-size:46px;font-weight:700;color:var(--navy);line-height:56px}
.portfolio-intro{left:280px;top:870px;width:640px;text-align:center;font-size:14px;font-weight:300;color:var(--navy);line-height:15.5px}
.work-card{top:952px;height:260px;text-align:left}
.work-card .media{height:218px}
.work-name{margin:10px 0 0 5px;font-size:15px;font-weight:700;color:var(--navy);white-space:nowrap;letter-spacing:-.2px}
.client{margin-left:5px;font-size:9px;color:var(--grey)}
</style>
</head>
<body>
<div class="abs top-strip"></div>

<section class="abs products" aria-label="Custom software"></section>
<h2 class="abs section-title">SOME OF OUR CUSTOM SOFTWARE FOR ENTERPRISE</h2>
<div class="abs nav-arrows" style="left:923px;top:57px">
  <svg viewBox="0 0 20 20"><circle cx="10" cy="10" r="9" fill="none" stroke="#1b7585" stroke-width="1.2"/><path d="M11.5 6 7.5 10l4 4" fill="none" stroke="#1b7585" stroke-width="1.2"/></svg>
  <svg viewBox="0 0 20 20"><circle cx="10" cy="10" r="9" fill="none" stroke="#1b7585" stroke-width="1.2"/><path d="M8.5 6l4 4-4 4" fill="none" stroke="#1b7585" stroke-width="1.2"/></svg>
</div>

<div class="abs card product-card" style="left:230px">
  <div class="media" role="img" aria-label="Globe with connected platform icons" style="background:radial-gradient(circle at 40% 55%,#e8f7ff,#5cb8ec 35%,transparent 60%),linear-gradient(135deg,#bfe9fb,#2a8fd6 60%,#0f5ba8)"></div>
  <div class="product-name">INTRANET SYSTEMS</div><div class="starting">STARTING FROM</div>
  <div class="price">$840</div><span class="shop">SHOP NOW!</span>
</div>
<div class="abs card product-card" style="left:417px">
  <div class="media" role="img" aria-label="Keyboard and mouse with globe" style="background:radial-gradient(circle at 70% 70%,#dceefb,transparent 45%),linear-gradient(135deg,#eaf3fb,#8fbfe6 50%,#2d6fbf)"></div>
  <div class="product-name">BACKLIT TOOL</div><div class="starting">STARTING FROM</div>
  <div class="price">$125</div><span class="shop">SHOP NOW!</span>
</div>
<div class="abs card product-card" style="left:604px">
  <div class="media" role="img" aria-label="Laptop with floating media screens" style="background:radial-gradient(circle at 50% 45%,#f4f8fc,#9cc0e0 35%,transparent 60%),linear-gradient(135deg,#5a7fa8,#7fa8cf 55%,#1e2a3c)"></div>
  <div class="product-name">MONITORING OFFLINE</div><div class="starting">STARTING FROM</div>
  <div class="price">$565</div><span class="shop">SHOP NOW!</span>
</div>
<div class="abs card product-card" style="left:791px">
  <div class="media" role="img" aria-label="Colourful binary digits on a neon grid" style="background:radial-gradient(circle at 55% 40%,rgba(220,40,120,.55),transparent 45%),radial-gradient(circle at 75% 80%,rgba(120,220,40,.5),transparent 45%),linear-gradient(135deg,#1a1030,#14386e 50%,#0c4a2a)"></div>
  <div class="product-name">WEB PRESENTATIONS</div><div class="starting">STARTING FROM</div>
  <div class="price">$250</div><span class="shop">SHOP NOW!</span>
</div>

<section class="abs testimonial" role="img" aria-label="Business handshake in blue tone"></section>
<div class="abs avatar" role="img" aria-label="Portrait of the client"></div>
<div class="abs person person-name">MARTIN ALDOUS</div>
<div class="abs person person-role">CCO / VELNARO</div>
<p class="abs quote">"Lorem ipsum dolor sit amet, consectetur adipisicing elit, sed do eiusmod tempor incididunt ut labore et dolore magna aliqua. Ut enim ad minim veniam, quis nostrud exercitation ullamco laboris nisi ut aliquip ex ea commodo consequat."</p>
<div class="abs dots"><span></span><span></span><span></span><span></span><span class="dim"></span><span></span></div>

<section class="abs portfolio" aria-label="Portfolio"></section>
<div class="abs portfolio-kicker">WIDE RANGE OF</div>
<h2 class="abs portfolio-title">PORTFOLIO</h2>
<p class="abs portfolio-intro">Lorem Ipsum is simply dummy text of the printing and typesetting industry. Lorem Ipsum has been the industry's standard dummy text ever since the 1500s, when an unknown printer took a galley of type and scrambled it to make a type specimen book.</p>
<div class="abs nav-arrows" style="left:923px;top:924px">
  <svg viewBox="0 0 20 20"><circle cx="10" cy="10" r="9" fill="none" stroke="#163c7c" stroke-width="1.2"/><path d="M11.5 6 7.5 10l4 4" fill="none" stroke="#163c7c" stroke-width="1.2"/></svg>
  <svg viewBox="0 0 20 20"><circle cx="10" cy="10" r="9" fill="none" stroke="#163c7c" stroke-width="1.2"/><path d="M8.5 6l4 4-4 4" fill="none" stroke="#163c7c" stroke-width="1.2"/></svg>
</div>

<div class="abs card work-card" style="left:230px">
  <div class="media" role="img" aria-label="Figures pulling a rope on a laptop with binary code" style="background:radial-gradient(ellipse at 60% 55%,#c9d3e8,transparent 35%),linear-gradient(160deg,#1d3fa8,#2a5fd0 50%,#0d1f5a)"></div>
  <div class="work-name">WEB PRESENTATIONS</div><div class="client">CLIENT NAME</div>
</div>
<div class="abs card work-card" style="left:417px">
  <div class="media" role="img" aria-label="Tablet showing bar and pie charts" style="background:radial-gradient(ellipse at 45% 45%,#e9f1f7,transparent 45%),linear-gradient(160deg,#5f86ad,#c9dbe9 50%,#eef2f5)"></div>
  <div class="work-name">OPTIMALIZATION</div><div class="client">CLIENT NAME</div>
</div>
<div class="abs card work-card" style="left:604px">
  <div class="media" role="img" aria-label="Hands typing on a keyboard" style="background:radial-gradient(ellipse at 65% 75%,#e8c9b4,transparent 40%),linear-gradient(160deg,#ffffff,#e6e6e6 50%,#b9b3a8)"></div>
  <div class="work-name">SIMULATION TOOLS</div><div class="client">CLIENT NAME</div>
</div>
<div class="abs card work-card" style="left:791px">
  <div class="media" role="img" aria-label="Engineer with tablet in a server room" style="background:radial-gradient(ellipse at 45% 55%,#5a4a40,transparent 45%),linear-gradient(160deg,#0a1430,#1d3560 50%,#3a4a5a)"></div>
  <div class="work-name">ENTERPRISE SYSTEMS</div><div class="client">CLIENT NAME</div>
</div>
</body>
</html>
```